"Velvet Crest" sexual performance enhancement pill bottle label needed.

This should be interesting...

I am starting a line of sexual performance enhancement products. This will be the first of several products basically. Keep in mind, I am the type of business person to stay with one company for years if they provide me with quality work.

This particular product is a male sexual performance pill. The name of the product is "Velvet Crest." The packaging of the pills are a black bottle with a white top. Label on the product example would be perfect but at a minimum I have attached a "template" for your guidance.

Some of the technical aspects of this are as follows:

-File Format: Illustrator CS6 is preferred. (Winner must provide artwork in layer and can not flatten artwork.)
-Resolution: 300 dpi minimum
-Bleed: 1/16th (0.0625") inch from edge of label
-Color Mode: CMYK only or must be converted to CMYK for final production

Lastly, this is your project as a designer, artist, creator, this is essentially a piece of you that will be sold and known by thousands of people. I have no color scheme that I prefer, just use the template and follow the layout. If you have any further questions, please feel free to contact me at any time.
Updates

Quick note on the product and what it does: -Powerful, long lasting, harder erections -Works in a minutes and last for hours -Enhances sexual desire and drive Thank you for your ideas...

Project Deadline Extended
Reason: We decided to extent the project for a few more days to let the last few concepts come in. So far things are looking really good and we definitely have seen some amazing designs. Thank you for your hard work and amazing creativity. Looking forward to seeing what we have come in the next couple of day. Very respectfully, Brock

ONLY THREE DAYS LEFT!!!! Please submit your ideas as soon as possible. And as always, thank you for your help!!! V/r, Brock

Industry/Entity Type

Graphic Design

```html
<!DOCTYPE html>
<html lang="en">
<head>
<meta charset="utf-8">
<title>Velvet Crest – Horny Goat Weed 1600 Label</title>
<link href="https://fonts.googleapis.com/css2?family=Fira+Sans:wght@400;500&display=swap" rel="stylesheet">
<style>
  :root {
    --backdrop: #3a3a3a;
    --label-black: #0b0b0b;
    --label-edge: #1c1c1c;
    --text-white: #f4f4f4;
    --text-soft: #cfcfcf;
    --brand-grey: #8d8d8d;
    --arc-grey: #6a6a6a;
  }
  * { margin: 0; padding: 0; box-sizing: border-box; }
  html, body {
    width: 1200px;
    height: 900px;
    overflow: hidden;
    background: var(--backdrop);
    font-family: "Fira Sans", sans-serif;
  }
  .canvas {
    position: relative;
    width: 1200px;
    height: 900px;
    display: flex;
    align-items: center;
    justify-content: center;
  }
  .label {
    position: relative;
    width: 700px;
    height: 520px;
    background: var(--label-black);
    border: 1px solid var(--label-edge);
    color: var(--text-white);
    text-align: center;
  }
  .brand-name {
    position: absolute;
    top: 70px;
    left: 0;
    right: 0;
    font-size: 40px;
    font-weight: 500;
    letter-spacing: 1px;
    color: var(--brand-grey);
  }
  .shield-arc {
    position: absolute;
    left: 150px;
    top: 130px;
    width: 200px;
    height: 280px;
  }
  .product-title {
    position: absolute;
    top: 150px;
    left: 0;
    right: 0;
    font-size: 54px;
    font-weight: 400;
    line-height: 1.02;
  }
  .strength {
    position: absolute;
    top: 338px;
    left: 0;
    right: 0;
    font-size: 20px;
    font-weight: 400;
  }
  .claim {
    position: absolute;
    top: 412px;
    left: 0;
    right: 0;
    font-size: 20px;
    font-weight: 500;
  }
  .claim sup { font-size: 12px; }
  .contents {
    position: absolute;
    top: 450px;
    left: 0;
    right: 0;
    font-size: 20px;
    color: var(--text-soft);
  }
</style>
</head>
<body>
  <main class="canvas">
    <section class="label">
      <div class="brand-name">Velvet Crest</div>
      <svg class="shield-arc" viewBox="0 0 200 280" aria-hidden="true">
        <path d="M40 20 C 22 110, 40 195, 130 245" fill="none" stroke="var(--arc-grey)" stroke-width="3" stroke-linecap="round"/>
      </svg>
      <h1 class="product-title">Horny<br>Goat Weed<br>1600</h1>
      <p class="strength">Max Strength!</p>
      <p class="claim">Pure and Potent<sup>*</sup></p>
      <p class="contents">Dietary Supplement · 60 Capsules</p>
    </section>
  </main>
</body>
</html>
```